SPLIT SCREEN SPLASH PAGE DESIGN

when people type in my website
id like a creative design for them to chose a destination

the choices are Brooklyn or Harlem

I've added our logo here
and I've added something we previously had designed
for a similar idea .... but we wound up not liking this

I've added some styles we do like ...

Industry/Entity Type

event rentals

Font styles to use
Serif

```html
<!DOCTYPE html>
<html lang="en">
<head>
<meta charset="UTF-8">
<title>Choose Your Destination — Brooklyn or Harlem</title>
<link rel="stylesheet" href="https://fonts.googleapis.com/css2?family=Archivo:wdth,wght@100,400;100,500;125,900&family=Kaushan+Script&display=swap">
<style>
  :root {
    --cyan: #45e6f5;
    --blue: #1f5fe0;
    --blue-deep: #2a4fd6;
    --yellow: #fff700;
    --amber: #ffb300;
    --navy: #1b1464;
    --orange: #f15a29;
    --white: #ffffff;
    --ink: #111111;
  }
  * { margin: 0; padding: 0; box-sizing: border-box; }
  html, body {
    width: 1200px; height: 675px; overflow: hidden; background: var(--white);
  }
  .splash {
    position: relative; width: 1200px; height: 675px; overflow: hidden;
    font-family: "Archivo", Arial, sans-serif;
  }
  .destination {
    position: absolute; top: 0; width: 600px; height: 675px; text-decoration: none;
  }
  .destination--brooklyn { left: 0; }
  .destination--harlem { left: 600px; }
  .scene-photo { position: absolute; inset: 0; }
  .destination--brooklyn .scene-photo {
    background: linear-gradient(180deg, var(--cyan) 0%, #3aa8ee 40%, var(--blue) 75%, var(--blue-deep) 100%);
  }
  .destination--harlem .scene-photo {
    background: linear-gradient(180deg, var(--yellow) 0%, #ffd600 45%, var(--amber) 100%);
  }
  .tagline {
    position: absolute; left: 283px; top: 125px; width: 634px; height: 58px; z-index: 2;
  }
  .tagline-band { position: absolute; inset: 0; }
  .tagline-text {
    position: relative; display: block; text-align: center;
    font-family: "Kaushan Script", cursive; font-size: 40px; line-height: 58px;
    color: var(--ink);
  }
  .place-name {
    position: absolute; font-weight: 900; font-stretch: 125%;
    font-size: 90px; line-height: 1; letter-spacing: -1px; white-space: nowrap;
  }
  .destination--brooklyn .place-name { color: var(--navy); }
  .destination--harlem .place-name { color: var(--orange); }
  .brooklyn-top { left: 106px; top: 270px; }
  .brooklyn-bottom { left: 223px; top: 353px; }
  .harlem-top { left: 106px; top: 270px; }
  .harlem-bottom { left: 240px; top: 353px; }
  .side-choice {
    position: absolute; top: 527px; width: 110px; height: 40px;
    display: flex; align-items: center; justify-content: center;
    font-size: 22px; font-weight: 500; letter-spacing: 3.5px; padding-left: 3px;
    color: var(--white);
  }
  .destination--brooklyn .side-choice { background: var(--orange); }
  .destination--harlem .side-choice { background: var(--navy); }
  .brooklyn-east { left: 169px; }
  .brooklyn-west { left: 298px; }
  .harlem-east { left: 181px; }
  .harlem-west { left: 311px; }
</style>
</head>
<body>
<main class="splash">
  <section class="destination destination--brooklyn">
    <div class="scene-photo" role="img" aria-label="Brooklyn street with brick warehouses framing the Manhattan Bridge, tinted blue"></div>
    <h2 class="place-name brooklyn-top">BROO</h2>
    <span class="place-name brooklyn-bottom" aria-hidden="true">KLYN</span>
    <a class="side-choice brooklyn-east" href="#brooklyn-east">EAST</a>
    <a class="side-choice brooklyn-west" href="#brooklyn-west">WEST</a>
  </section>

  <section class="destination destination--harlem">
    <div class="scene-photo" role="img" aria-label="Harlem elevated train tracks and skyline, tinted yellow and amber"></div>
    <h2 class="place-name harlem-top">HAR</h2>
    <span class="place-name harlem-bottom" aria-hidden="true">LEM</span>
    <a class="side-choice harlem-east" href="#harlem-east">EAST</a>
    <a class="side-choice harlem-west" href="#harlem-west">WEST</a>
  </section>

  <div class="tagline">
    <svg class="tagline-band" viewBox="0 0 634 58" preserveAspectRatio="none" aria-hidden="true">
      <path d="M8 10 Q320 0 626 6 L630 30 L620 52 Q320 60 14 50 L2 30 Z" fill="#ffffff"/>
    </svg>
    <h1 class="tagline-text">Celebrate all the moments</h1>
  </div>
</main>
</body>
</html>
```